Menu Board 1000mmx500mm re-design

I would like to re-design exiting menu board 1000mmx500mm. Current board letters are bit to small to read. I would like to have pictures (attached) of the food offered on it and at the same time to create balance between pictures and size of the text to be easily readable. Fonts and colours are up to designer choice but prefer warm and bright colours rather anything dark.

Target Market(s)

Food industry

Industry/Entity Type

Food

Font styles to use
Other font styles liked:
• I leave font choice to designer

Colors
FFC000
F8CF3A
FAE287
FDF2CF
FEFAEE
F0912C
F2A743
F7CA91
FBE8D2
FDF5EE
EE7325
F08F49
F5BC92
FAE3D3
FDF4ED

Requirements
Must have
• Pictures + Text
Nice to have
• Balance between images and text.
Should not have
• Can't think of any

```html
<!DOCTYPE html>
<html lang="en">
<head>
<meta charset="utf-8">
<title>Menu Board</title>
<link rel="stylesheet" href="https://fonts.googleapis.com/css2?family=Anton&family=Oswald:wght@500&family=Poppins:wght@500;700;800&family=Yellowtail&display=swap">
<style>
  :root {
    --amber: #FFC000;
    --sun: #FBC10A;
    --orange: #EE7325;
    --orange-soft: #F0912C;
    --orange-light: #F2A743;
    --brown: #6B3410;
    --ink: #2E2E2E;
    --white: #FFFFFF;
  }
  * { margin: 0; padding: 0; box-sizing: border-box; }
  html, body { width: 1200px; height: 2400px; overflow: hidden; background: var(--white); }
  .board { position: relative; width: 1200px; height: 2400px; overflow: hidden; font-family: "Poppins", sans-serif; color: var(--ink); }
  .band-orange { position: absolute; left: 0; top: 0; width: 1200px; height: 1160px; background: var(--orange); }
  .band-sun { position: absolute; left: 0; top: 0; width: 1200px; height: 720px;
    background: radial-gradient(circle at 20% 40%, #FFD21A 0%, var(--amber) 40%, var(--orange-soft) 100%); }
  .edge { position: absolute; left: 0; width: 1200px; }
  .hero-photo { position: absolute; left: 185px; top: 10px; width: 1015px; height: 670px;
    border-radius: 260px 120px 200px 300px;
    background: linear-gradient(160deg, #F3E3C4 0%, #E9C27A 35%, #5E8A3A 55%, #C9402E 70%, #EFD39A 100%); }
  .title-menu { position: absolute; left: 0; top: 740px; width: 1080px; text-align: center;
    font-family: "Yellowtail", cursive; font-size: 300px; line-height: 1; color: var(--white);
    text-shadow: 6px 6px 0 var(--brown), -4px -4px 0 var(--brown), 4px -4px 0 var(--brown), -4px 4px 0 var(--brown), 10px 10px 0 #2B1406; }
  .item { position: absolute; }
  .item-photo { position: absolute; width: 160px; height: 160px; border-radius: 50%;
    border: 5px solid var(--orange-soft); background: radial-gradient(circle, #C89060 0%, #8A5A34 55%, #EDEDED 56%, #F4F4F4 100%); }
  .item-name { position: absolute; font-weight: 800; font-size: 35px; line-height: 1.05; text-transform: uppercase; color: var(--ink); letter-spacing: 0.5px; }
  .item-desc { position: absolute; font-weight: 500; font-size: 24px; line-height: 1.2; color: var(--ink); }
  .price-tag { position: absolute; width: 70px; height: 68px; background: var(--orange);
    clip-path: polygon(0 0, 100% 0, 100% 100%, 50% 82%, 0 100%);
    color: var(--white); font-family: "Oswald", sans-serif; font-size: 30px; text-align: center; padding-top: 8px; }
  .price-tag sup { font-size: 16px; }
  .drink { position: absolute; height: 102px; border-radius: 24px; background: var(--orange-light);
    color: var(--white); font-weight: 800; font-size: 58px; line-height: 102px; padding-left: 34px; }
  .drink-price { position: absolute; top: 6px; width: 90px; height: 90px; border-radius: 50%;
    background: var(--orange); border: 3px solid var(--white); color: var(--white);
    font-family: "Oswald", sans-serif; font-size: 36px; line-height: 84px; text-align: center; font-weight: 500; }
  .drink-price sup { font-size: 18px; line-height: 0; }
  .band-yellow { position: absolute; left: 0; top: 1990px; width: 1200px; height: 410px; background: var(--sun); }
  .sauces-title { position: absolute; left: 0; top: 2070px; width: 1200px; text-align: center;
    font-family: "Anton", sans-serif; font-size: 96px; line-height: 1; color: #111; }
  .sauce { position: absolute; display: flex; align-items: center; gap: 26px;
    font-weight: 700; font-size: 36px; color: var(--ink); }
  .sauce svg { width: 46px; height: 46px; }
</style>
</head>
<body>
<div class="board">
  <div class="band-orange"></div>
  <div class="band-sun"></div>
  <svg class="edge" style="top:650px;height:110px" viewBox="0 0 1200 110" preserveAspectRatio="none">
    <path d="M0,110 L0,50 L40,44 L70,58 L110,40 L150,54 L190,30 L230,42 L260,20 L300,35 L1200,35 L1200,110 Z" fill="var(--orange)"/>
  </svg>
  <div class="hero-photo" role="img" aria-label="Grilled chicken wrap cut in half, filled with greens, tomato and red onion"></div>

  <div class="title-menu">Menu</div>

  <svg class="edge" style="top:1120px;height:60px" viewBox="0 0 1200 60" preserveAspectRatio="none">
    <path d="M0,60 L0,30 L60,24 L110,34 L170,18 L240,28 L300,20 L380,30 L450,16 L520,26 L600,14 L680,24 L760,8 L830,2 L880,14 L940,10 L1000,26 L1060,20 L1120,28 L1200,22 L1200,60 Z" fill="var(--white)"/>
  </svg>

  <!-- Row 1 -->
  <div class="item-photo" role="img" aria-label="Ciabatta sandwich on a wooden board" style="left:63px;top:1203px"></div>
  <div class="item-name" style="left:252px;top:1220px">Ciabatta</div>
  <div class="item-desc" style="left:252px;top:1263px">Roti Chicken, Rucola,<br>Caramelized Onions,<br>Tomato, Fresh Onion</div>
  <div class="price-tag" style="left:530px;top:1216px"><sup>£</sup>6</div>

  <div class="item-photo" role="img" aria-label="Toasted chicken wrap halves" style="left:615px;top:1190px"></div>
  <div class="item-name" style="left:793px;top:1210px">Wrap</div>
  <div class="item-desc" style="left:793px;top:1253px">Roti Chicken,<br>Crunchy Slaw, Tomato,<br>Fresh Onion &amp; Sauce of<br>your choice</div>
  <div class="price-tag" style="left:1066px;top:1216px"><sup>£</sup>7</div>

  <!-- Row 2 -->
  <div class="item-photo" role="img" aria-label="Beetroot wrap halves with salad" style="left:63px;top:1393px"></div>
  <div class="item-name" style="left:252px;top:1402px">Beetroot<br>Wrap</div>
  <div class="item-desc" style="left:252px;top:1487px">Roti Chicken, Crunchy<br>Slaw, Tomato,Fresh Onion<br>&amp; Sauce of your choice</div>
  <div class="price-tag" style="left:530px;top:1398px"><sup>£</sup>8</div>

  <div class="item-photo" role="img" aria-label="Quarter chicken with veggie rice in a wooden bowl" style="left:615px;top:1393px"></div>
  <div class="item-name" style="left:788px;top:1418px">1/4 Chicken<br>Box</div>
  <div class="item-desc" style="left:788px;top:1515px">Roti Chicken, Veggie<br>Rice &amp; Salad</div>
  <div class="price-tag" style="left:1066px;top:1406px"><sup>£</sup>9</div>

  <!-- Row 3 -->
  <div class="item-photo" role="img" aria-label="Half chicken with veggie rice in a wooden bowl" style="left:63px;top:1604px"></div>
  <div class="item-name" style="left:245px;top:1614px">1/2 Chicken<br>Box</div>
  <div class="item-desc" style="left:245px;top:1715px">Roti Chicken, Veggie<br>Rice &amp; Salad</div>
  <div class="price-tag" style="left:530px;top:1622px"><sup>£</sup>14</div>

  <div class="item-photo" role="img" aria-label="Golden roasted potatoes" style="left:615px;top:1604px;background:radial-gradient(circle,#F1B43C 0%,#C57A1C 60%,#F4F4F4 100%)"></div>
  <div class="item-name" style="left:790px;top:1630px">Roasted<br>Potatoes</div>
  <div class="item-desc" style="left:790px;top:1733px">Thyme &amp; Garlic</div>
  <div class="price-tag" style="left:1066px;top:1620px"><sup>£</sup>2.5</div>

  <!-- Drinks -->
  <div class="drink" style="left:107px;top:1846px;width:395px">WATER
    <div class="drink-price" style="left:295px"><sup>£</sup>1</div>
  </div>
  <div class="drink" style="left:522px;top:1846px;width:590px;padding-left:14px">CAN &amp; JUICES
    <div class="drink-price" style="left:490px"><sup>£</sup>1.8</div>
  </div>

  <!-- Sauces -->
  <div class="band-yellow"></div>
  <svg class="edge" style="top:1960px;height:60px" viewBox="0 0 1200 60" preserveAspectRatio="none">
    <path d="M0,0 L1200,0 L1200,20 L1150,26 L1100,44 L1040,36 L980,52 L920,40 L860,34 L800,46 L740,38 L680,50 L620,42 L560,30 L500,38 L440,26 L380,34 L320,24 L260,32 L200,22 L140,30 L80,20 L0,28 Z" fill="var(--white)"/>
  </svg>
  <div class="sauces-title">SAUCES</div>

  <div class="sauce" style="left:104px;top:2193px"><svg viewBox="0 0 46 46"><circle cx="23" cy="23" r="23" fill="var(--orange-soft)"/><path d="M13 23 L20 30 L33 16" stroke="#FBC10A" stroke-width="4" fill="none" stroke-linecap="round" stroke-linejoin="round"/></svg><span style="margin-left:10px">SIGNATURE</span></div>
  <div class="sauce" style="left:480px;top:2193px"><svg viewBox="0 0 46 46"><circle cx="23" cy="23" r="23" fill="var(--orange-soft)"/><path d="M13 23 L20 30 L33 16" stroke="#FBC10A" stroke-width="4" fill="none" stroke-linecap="round" stroke-linejoin="round"/></svg><span style="margin-left:10px">GARLIC MAYO</span></div>
  <div class="sauce" style="left:885px;top:2193px"><svg viewBox="0 0 46 46"><circle cx="23" cy="23" r="23" fill="var(--orange-soft)"/><path d="M13 23 L20 30 L33 16" stroke="#FBC10A" stroke-width="4" fill="none" stroke-linecap="round" stroke-linejoin="round"/></svg><span style="margin-left:10px">BBQ</span></div>
  <div class="sauce" style="left:230px;top:2268px"><svg viewBox="0 0 46 46"><circle cx="23" cy="23" r="23" fill="var(--orange-soft)"/><path d="M13 23 L20 30 L33 16" stroke="#FBC10A" stroke-width="4" fill="none" stroke-linecap="round" stroke-linejoin="round"/></svg><span style="margin-left:10px">SWEET CHILLI</span></div>
  <div class="sauce" style="left:655px;top:2268px"><svg viewBox="0 0 46 46"><circle cx="23" cy="23" r="23" fill="var(--orange-soft)"/><path d="M13 23 L20 30 L33 16" stroke="#FBC10A" stroke-width="4" fill="none" stroke-linecap="round" stroke-linejoin="round"/></svg><span style="margin-left:10px">PIRI PIRI</span></div>
</div>
</body>
</html>
```